Chat Software Business Card Design

We need a business card design for our company.

We provide businesses with a platform to communicate with their web visitors in real time using chat boxes on their web sites.

We're using a bright color scheme to attract attention on the site and the business card would do well to reflect this also to maintain brand awareness. However it is not essential to the ultimate design to use the same color scheme or feel as the site.

We offer a Free Trial of the software and would encourage a business card design to promote this if possible.

http://qelmarworks7.co.uk/projects/guest/index2.html

You will find the company logo attached also.

An eye catching design with something that will set the card apart from others is required.

The design of the card/theme of the card should be very unique, setting our selves apart, eye catching whilst not providing a "wacky" image for the company.

It should also include our contact information;~
Website - www.talkpond-live.com
Email - support@talkpond-live.com
Twitter - @Talkpondlive

Industry/Entity Type

Software

Contact Information for Business Card

Web - www.talkpond-live.com
Email - office@talkpond-live.com
Skype - Talkpond.Live

Requirements
Must have
• Use of company logo is required.

```html
<!DOCTYPE html>
<html lang="en">
<head>
<meta charset="utf-8">
<title>Talkpond Live – Business Card</title>
<link href="https://fonts.googleapis.com/css2?family=Arimo:wght@400;700&display=swap" rel="stylesheet">
<style>
  :root {
    --orange-deep: #f05a30;
    --orange-mid: #f47c35;
    --orange-light: #fbb040;
    --paper: #ffffff;
    --ink: #1a1a1a;
    --stage: #ffffff;
  }
  * { margin: 0; padding: 0; box-sizing: border-box; }
  html, body {
    width: 886px; height: 1200px; overflow: hidden;
    background: var(--stage);
    font-family: "Arimo", Arial, sans-serif;
  }
  .canvas { position: relative; width: 886px; height: 1200px; }
  .card {
    position: absolute; left: 32px; width: 815px; height: 538px;
    box-shadow: 0 2px 10px rgba(0,0,0,0.35);
    overflow: hidden;
  }
  .card--front {
    top: 50px;
    background: radial-gradient(ellipse 48% 58% at 47% 55%, var(--orange-light) 0%, var(--orange-mid) 55%, var(--orange-deep) 100%);
    display: flex; align-items: center; justify-content: center;
  }
  .brand-name {
    color: var(--paper); font-weight: 700; font-size: 84px; letter-spacing: -1px;
    white-space: nowrap;
  }
  .card--back { top: 626px; background: var(--paper); }
  .brand-band {
    position: absolute; left: 0; top: 202px; width: 436px; height: 142px;
    background: linear-gradient(90deg, var(--orange-deep) 0%, var(--orange-mid) 45%, var(--orange-light) 100%);
    display: flex; align-items: center; justify-content: center;
  }
  .brand-band .brand-name { font-size: 42px; }
  .contact-list {
    position: absolute; left: 454px; top: 202px; list-style: none;
  }
  .contact-item {
    display: flex; align-items: center; height: 20px; margin-bottom: 20px;
    font-size: 13px; color: var(--ink);
  }
  .contact-item:nth-child(3) { margin-top: 2px; }
  .contact-icon { width: 20px; height: 20px; margin-right: 13px; flex: none; }
</style>
</head>
<body>
<div class="canvas">
  <section class="card card--front">
    <div class="brand-name">Talkpond Live</div>
  </section>

  <section class="card card--back">
    <div class="brand-band">
      <div class="brand-name">Talkpond Live</div>
    </div>
    <ul class="contact-list">
      <li class="contact-item">
        <svg class="contact-icon" viewBox="0 0 20 20" aria-hidden="true">
          <rect x="1" y="4" width="18" height="12" fill="var(--orange-deep)"/>
          <path d="M1 4 L10 11 L19 4" fill="none" stroke="#fff" stroke-width="1.4"/>
        </svg>
        office@talkpond-live.com
      </li>
      <li class="contact-item">
        <svg class="contact-icon" viewBox="0 0 20 20" aria-hidden="true">
          <g fill="none" stroke="var(--orange-deep)" stroke-width="1.6">
            <circle cx="10" cy="10" r="8.5"/>
            <ellipse cx="10" cy="10" rx="3.8" ry="8.5"/>
            <line x1="1.5" y1="10" x2="18.5" y2="10"/>
            <path d="M3 5.5 H17 M3 14.5 H17"/>
          </g>
        </svg>
        www.talkpond-live.com
      </li>
      <li class="contact-item">
        <svg class="contact-icon" viewBox="0 0 20 20" aria-hidden="true">
          <circle cx="10" cy="10" r="9" fill="var(--orange-deep)"/>
        </svg>
        Talkpond.Live
      </li>
      <li class="contact-item">
        <svg class="contact-icon" viewBox="0 0 20 20" aria-hidden="true">
          <circle cx="10" cy="10" r="9" fill="var(--orange-deep)"/>
        </svg>
        @Talkpondlive
      </li>
    </ul>
  </section>
</div>
</body>
</html>
```